Photo-Video Combo Package Flyer

Need to create a flyer to showcase a combo package featuring photography and videography from two separate companies. I need an 8 1/2 X 11 flyer in .psd so I can make changes as needed as well as all fonts
Target Market(s)
Brides & Grooms
Industry/Entity Type
Wedding Photography
Requirements
Must have
- see word doc
Nice to have
- please visit websites for inspiration
- https://brightoakportraitstudio.com/
- www.qmtrz.com

```html
<!DOCTYPE html>
<html lang="en">
<head>
<meta charset="utf-8">
<title>Photo + Video Combo Package</title>
<link href="https://fonts.googleapis.com/css2?family=Libre+Baskerville:ital,wght@0,400;1,400&family=Montserrat:wght@500;700&family=Raleway:wght@400;600;700&display=swap" rel="stylesheet">
<style>
  :root {
    --ink: #555352;
    --ink-dark: #1c1c1c;
    --peach: #f5d6c8;
    --paper: #ffffff;
    --badge: #fad24c;
    --haze: #f1f1f1;
    --brand: #c98f86;
  }
  html, body { margin: 0; padding: 0; overflow: hidden; }
  body { width: 927px; height: 1200px; }
  .flyer {
    position: relative; width: 927px; height: 1200px; overflow: hidden;
    background: linear-gradient(to bottom, var(--paper) 0, var(--paper) 840px, var(--peach) 1200px);
    font-family: "Raleway", sans-serif; color: var(--ink);
    font-variant-numeric: lining-nums;
  }
  .background-haze {
    position: absolute; left: 0; top: 20px; width: 330px; height: 520px;
    background: radial-gradient(ellipse at 30% 50%, var(--haze) 0, rgba(241,241,241,0) 70%);
  }
  .intro {
    position: absolute; right: 64px; top: 82px; margin: 0;
    text-align: right; font-family: "Libre Baskerville", serif; font-style: italic;
    font-size: 25px; line-height: 30px; color: var(--ink); white-space: nowrap;
  }
  .intro p { margin: 0 0 60px; }
  .package { position: absolute; right: 69px; top: 414px; text-align: right; font-size: 18px; line-height: 21.8px; letter-spacing: .4px; }
  .package h3 { margin: 0; font-size: 17px; font-weight: 700; letter-spacing: .2px; }
  .package ul { list-style: none; margin: 0; padding: 0; }
  .package li::before { content: "• "; }
  .provider { position: absolute; left: 67px; }
  .provider h2 { margin: 0; font-family: "Montserrat", sans-serif; font-size: 24px; line-height: 28px; color: var(--ink-dark); letter-spacing: .3px; }
  .provider p { margin: 2px 0 0; font-family: "Libre Baskerville", serif; font-style: italic; font-size: 14px; line-height: 19px; color: var(--ink-dark); }
  .provider--photo { top: 544px; }
  .provider--video { top: 644px; }
  .combo-title { position: absolute; left: 642px; top: 630px; margin: 0; font-family: "Montserrat", sans-serif; font-size: 30px; color: var(--ink-dark); }
  .photo { position: absolute; border: 3px solid var(--paper); box-sizing: border-box; }
  .photo--sunset { left: 336px; top: 612px; width: 248px; height: 121px; background: linear-gradient(to bottom, #b79a8f 0, #f2a65a 55%, #5a6d80 100%); }
  .photo--deck { left: 240px; top: 734px; width: 252px; height: 109px; background: linear-gradient(to bottom, #8a8fb3, #d7a4b4 50%, #6d6d86); }
  .photo--harbor { left: 494px; top: 734px; width: 176px; height: 109px; background: linear-gradient(to bottom, #6f6a74, #c59a78 60%, #4a4a50); }
  .photo--forest { left: 112px; top: 843px; width: 250px; height: 142px; background: linear-gradient(135deg, #1f3326, #4c6b45 60%, #c9a75c); }
  .photo--portrait { left: 362px; top: 843px; width: 220px; height: 110px; background: linear-gradient(to right, #d9d2cc, #c4826f 50%, #e4ddd6); }
  .photo--pier { left: 582px; top: 843px; width: 228px; height: 142px; background: linear-gradient(to bottom, #5d6790, #b8a2b8 55%, #2f7f8f); }
  .badge { position: absolute; left: 664px; top: 694px; width: 196px; height: 196px; }
  .badge-text { font-family: "Montserrat", sans-serif; font-weight: 700; fill: var(--ink-dark); }
  .badge-price { font-family: "Montserrat", sans-serif; font-weight: 500; fill: var(--ink-dark); }
  .brand-oval { position: absolute; left: 240px; top: 930px; width: 450px; height: 150px; }
  .brand-name {
    position: absolute; left: 240px; top: 980px; width: 450px; text-align: center;
    font-family: "Raleway", sans-serif; font-weight: 600; font-size: 24px; color: var(--brand); margin: 0;
  }
  .contact { position: absolute; left: 0; right: 0; top: 1081px; text-align: center; }
  .contact strong { display: block; font-size: 19px; font-weight: 700; }
  .contact span { display: block; margin-top: 11px; font-size: 17px; }
</style>
</head>
<body>
<main class="flyer">
  <div class="background-haze" aria-hidden="true"></div>

  <div class="intro">
    <p>The Photo-Video combo package is the best way<br>to hire your Photographer and videographer.<br>Both companies are highly rated by The Vow Guide<br>and Wedding Circle as well as recommended<br>by the area’s top wedding venues.</p>
    <p>When your photographer and videographer are<br>working together your wedding day will run<br>smoothly, so you can just enjoy<br>yourself and have fun!</p>
  </div>

  <section class="package">
    <h3>Photo Package Includes:</h3>
    <ul>
      <li>1 Hr Engagement Shoot</li>
      <li>One photographer up to 7 hours on location for wedding</li>
      <li>High Resolution, Edited digital images</li>
      <li>Images professionally edited in house</li>
      <li>Beautiful online gallery to download from</li>
      <li>Print release to print at the lab of your choice</li>
      <li>Normal Retail Price $2450</li>
    </ul>
  </section>

  <div class="provider provider--photo"><h2>PHOTOGRAPHY</h2><p>provided by<br>Bright Oak Portrait Studio</p></div>
  <div class="provider provider--video"><h2>VIDEOGRAPHY</h2><p>provided by<br>Quartzmotion Films</p></div>

  <h2 class="combo-title">PHOTO+VIDEO</h2>

  <div class="photo photo--sunset" role="img" aria-label="Couple kissing at sunset by the sea"></div>
  <div class="photo photo--deck" role="img" aria-label="Couple on a ship deck under a pink sky"></div>
  <div class="photo photo--harbor" role="img" aria-label="Couple by a harbor lamp post at dusk"></div>
  <div class="photo photo--forest" role="img" aria-label="Couple on a wooden bridge among trees at night"></div>
  <div class="photo photo--portrait" role="img" aria-label="Bridal portrait"></div>
  <div class="photo photo--pier" role="img" aria-label="Couple on a pier at twilight"></div>

  <svg class="badge" viewBox="0 0 196 196" aria-label="Combo $2999, save $750">
    <circle cx="102" cy="102" r="92" fill="#cfcfcf" opacity=".6"/>
    <circle cx="96" cy="96" r="92" fill="var(--badge)"/>
    <path d="M150 40 A78 78 0 0 1 120 170" fill="none" stroke="var(--ink-dark)" stroke-width="2"/>
    <g transform="rotate(-22 96 96)">
      <text class="badge-text" x="90" y="72" font-size="20" text-anchor="middle" letter-spacing="1">COMBO</text>
      <text class="badge-price" x="96" y="116" font-size="44" text-anchor="middle">$2999</text>
      <text class="badge-text" x="100" y="142" font-size="17" text-anchor="middle">(SAVE $750)</text>
    </g>
  </svg>

  <svg class="brand-oval" viewBox="0 0 450 150" aria-hidden="true">
    <ellipse cx="225" cy="78" rx="222" ry="68" fill="var(--paper)" transform="rotate(-3 225 78)"/>
  </svg>
  <p class="brand-name">Bright Oak Portrait Studio</p>

  <div class="contact">
    <strong>Contact us to learn more and schedule a consultation</strong>
    <span>brightoakportraitstudio.com</span>
  </div>
</main>
</body>
</html>
```